KerrLow Farm

Need a nice simple clean double sided business card that has our logo and info on:
Kerr Low Farm
Martin & Felicity Kerr Low
kerrlowfarm@mailbarn.example
Martin: 1-780-555-0148
Felicity: 1-780-555-0193
Instagram @ kerrlow_farm

Contact Information for Business Card

Martin & Felicity Kerr Low kerrlowfarm@mailbarn.example Martin: 1-780-555-0148 Felicity: 1-780-555-0193

```html
<!DOCTYPE html>
<html lang="en">
<head>
<meta charset="utf-8">
<title>Kerr Low Farm — Business Card</title>
<link rel="stylesheet" href="https://fonts.googleapis.com/css2?family=Roboto:wght@400;700&display=swap">
<style>
  :root {
    --bg: #e6e6e4;
    --card: #ffffff;
    --green: #5fa13c;
    --orange: #f5a10f;
    --ink: #3a3a3a;
  }
  html, body {
    margin: 0;
    width: 1200px;
    height: 900px;
    overflow: hidden;
    background: var(--bg);
    font-family: "Roboto", sans-serif;
  }
  .stage {
    width: 1200px;
    height: 900px;
    display: flex;
    flex-direction: column;
    align-items: center;
    justify-content: center;
    gap: 48px;
  }
  .card {
    position: relative;
    width: 640px;
    height: 366px;
    background: var(--card);
    border-radius: 26px;
    overflow: hidden;
    box-shadow: 0 6px 18px rgba(0,0,0,0.12);
    display: flex;
    flex-direction: column;
    align-items: center;
  }
  .card-band {
    position: absolute;
    left: 0; right: 0; bottom: 0;
    height: 16px;
    background: var(--green);
    border-top: 4px solid var(--orange);
  }
  .brand {
    display: flex;
    align-items: center;
    gap: 16px;
  }
  .brand-mark {
    width: 58px;
    height: 58px;
    border: 4px solid var(--green);
    border-radius: 50%;
    box-sizing: border-box;
  }
  .brand-name {
    font-weight: 700;
    color: var(--green);
    font-size: 40px;
    letter-spacing: 1px;
    text-transform: uppercase;
  }
  .card-front { justify-content: center; padding-bottom: 20px; box-sizing: border-box; }
  .card-back { padding-top: 52px; box-sizing: border-box; }
  .card-back .brand-mark { width: 48px; height: 48px; }
  .card-back .brand-name { font-size: 32px; }
  .owners {
    margin-top: 34px;
    font-weight: 700;
    color: var(--green);
    font-size: 25px;
    text-transform: uppercase;
    letter-spacing: 0.3px;
  }
  .contacts {
    margin-top: 26px;
    display: grid;
    grid-template-columns: auto auto;
    column-gap: 34px;
    row-gap: 10px;
    font-size: 17px;
    color: var(--ink);
  }
  .contact { display: flex; align-items: center; gap: 8px; }
  .contact svg { width: 16px; height: 16px; flex: none; }
  .social-mark {
    width: 12px; height: 12px;
    border: 2px solid var(--orange);
    border-radius: 3px;
    flex: none;
  }
</style>
</head>
<body>
<main class="stage">
  <section class="card card-front">
    <div class="brand">
      <span class="brand-mark"></span>
      <span class="brand-name">Kerr Low Farm</span>
    </div>
    <div class="card-band"></div>
  </section>

  <section class="card card-back">
    <div class="brand">
      <span class="brand-mark"></span>
      <span class="brand-name">Kerr Low Farm</span>
    </div>
    <div class="owners">Martin &amp; Felicity Kerr Low</div>
    <div class="contacts">
      <div class="contact">
        <svg viewBox="0 0 24 24" aria-hidden="true"><path fill="var(--orange)" d="M6.6 10.8a15.1 15.1 0 0 0 6.6 6.6l2.2-2.2c.3-.3.7-.4 1-.2 1.1.4 2.3.6 3.6.6.6 0 1 .4 1 1V20c0 .6-.4 1-1 1A17 17 0 0 1 3 4c0-.6.4-1 1-1h3.5c.6 0 1 .4 1 1 0 1.3.2 2.5.6 3.6.1.3 0 .7-.2 1z"/></svg>
        <span>1-780-555-0148 (Martin)</span>
      </div>
      <div class="contact">
        <svg viewBox="0 0 24 24" aria-hidden="true"><path fill="var(--orange)" d="M6.6 10.8a15.1 15.1 0 0 0 6.6 6.6l2.2-2.2c.3-.3.7-.4 1-.2 1.1.4 2.3.6 3.6.6.6 0 1 .4 1 1V20c0 .6-.4 1-1 1A17 17 0 0 1 3 4c0-.6.4-1 1-1h3.5c.6 0 1 .4 1 1 0 1.3.2 2.5.6 3.6.1.3 0 .7-.2 1z"/></svg>
        <span>1-780-555-0193 (Felicity)</span>
      </div>
      <div class="contact">
        <svg viewBox="0 0 24 24" aria-hidden="true"><rect x="2" y="5" width="20" height="14" rx="1.5" fill="var(--orange)"/><path d="M3 6l9 7 9-7" fill="none" stroke="#fff" stroke-width="1.8"/></svg>
        <span>kerrlowfarm@mailbarn.example</span>
      </div>
      <div class="contact">
        <span class="social-mark"></span>
        <span>@kerrlow_farm</span>
      </div>
    </div>
    <div class="card-band"></div>
  </section>
</main>
</body>
</html>
```